Orvel Crest Holdings Ltd
Creative Brief
Dara Kolby
COO
27B Hollin Row, London, E3 9TQ
dk@orvelcrest.co.uk
27b Hollin Row
Just the logo and the company's name on the green background

```html
<!DOCTYPE html>
<html lang="en">
<head>
<meta charset="utf-8">
<title>Orvel Crest Holdings Ltd — Stationery</title>
<link href="https://fonts.googleapis.com/css2?family=Montserrat:wght@400;500;600&display=swap" rel="stylesheet">
<style>
  :root {
    --olive: #3b3c2d;
    --gold: #b99b5f;
    --paper: #ffffff;
    --backdrop: #ffffff;
    --ink: #6b6b66;
    --ink-light: #a3a39e;
  }
  * { margin: 0; padding: 0; box-sizing: border-box; }
  html, body { width: 1200px; height: 770px; overflow: hidden; background: var(--backdrop); }
  body { position: relative; font-family: "Montserrat", sans-serif; color: var(--ink); }

  .sheet { position: absolute; background: var(--paper); box-shadow: 0 2px 10px rgba(0,0,0,0.12); overflow: hidden; }

  .brand { display: flex; align-items: center; gap: 5px; color: var(--gold); font-weight: 600; letter-spacing: 0.08em; text-transform: uppercase; white-space: nowrap; }
  .brand-dot { border-radius: 50%; background: var(--gold); flex: none; }
  .brand-stack { flex-direction: column; gap: 3px; text-align: center; line-height: 1.25; }

  /* Letterhead */
  .letterhead { left: 168px; top: 144px; width: 432px; height: 476px; }
  .letterhead .band { position: absolute; left: 0; top: 0; width: 60px; height: 100%; background: var(--olive); }
  .letterhead .brand { position: absolute; left: 0; top: 26px; width: 60px; font-size: 5px; }
  .letterhead .brand-dot { width: 16px; height: 16px; }
  .contact { position: absolute; top: 30px; font-size: 4.5px; line-height: 7px; padding-left: 6px; border-left: 1.5px solid var(--gold); }
  .contact-person { left: 218px; }
  .contact-person strong { color: var(--olive); font-weight: 600; text-transform: uppercase; letter-spacing: 0.05em; }
  .contact-office { left: 282px; }
  .letter-date { position: absolute; right: 40px; top: 104px; font-size: 4.5px; }
  .letter-body { position: absolute; left: 84px; top: 138px; width: 300px; font-size: 4.5px; line-height: 7px; color: var(--ink-light); }
  .letter-body p { margin-bottom: 9px; }
  .letter-body .salutation { color: var(--ink); margin-bottom: 22px; }
  .signature { position: absolute; left: 330px; top: 362px; width: 50px; height: 18px; background: linear-gradient(90deg, rgba(185,155,95,0.55), rgba(185,155,95,0.25)); border-radius: 9px; }

  /* Business cards */
  .card-front { left: 667px; top: 144px; width: 185px; height: 96px; background: var(--olive); display: flex; align-items: center; justify-content: center; }
  .card-front .brand { font-size: 6px; gap: 4px; }
  .card-front .brand-dot { width: 22px; height: 22px; }
  .card-back { left: 864px; top: 149px; width: 192px; height: 91px; }
  .card-back .band { position: absolute; left: 0; top: 0; width: 48px; height: 100%; background: var(--olive); }
  .card-back .details { position: absolute; left: 62px; top: 16px; font-size: 4.5px; line-height: 7px; }
  .card-back .details strong { display: block; color: var(--olive); font-size: 5.5px; font-weight: 600; text-transform: uppercase; letter-spacing: 0.05em; }
  .card-back .rule { width: 18px; height: 1.5px; background: var(--gold); margin: 4px 0; }

  /* Envelope */
  .envelope { left: 667px; top: 300px; width: 418px; height: 144px; }
  .envelope .flap { position: absolute; left: 0; top: 0; width: 100%; height: 52px; }
  .envelope .brand { position: absolute; left: 50%; top: 10px; transform: translateX(-50%); font-size: 6px; }
  .envelope .brand-dot { width: 14px; height: 14px; }

  /* Compliment slip */
  .comp-slip { left: 667px; top: 475px; width: 178px; height: 145px; }
  .comp-slip .band { position: absolute; left: 0; top: 0; width: 44px; height: 100%; background: var(--olive); }
  .comp-slip .brand { position: absolute; left: 0; top: 26px; width: 44px; font-size: 4.5px; }
  .comp-slip .brand-dot { width: 12px; height: 12px; }
</style>
</head>
<body>

<section class="sheet letterhead" aria-label="Letterhead">
  <div class="band"></div>
  <div class="brand brand-stack"><span class="brand-dot"></span><span>Orvel<br>Crest</span></div>
  <div class="contact contact-person"><strong>Dara Kolby</strong><br>COO</div>
  <div class="contact contact-office">27B Hollin Row, London, E3 9TQ<br>dk@orvelcrest.co.uk<br>orvelcrest.co.uk</div>
  <div class="letter-date">20 March 2024</div>
  <div class="letter-body">
    <p class="salutation">Dear Client,</p>
    <p>Thank you for your interest in our holdings. We look forward to working with you on the next stage of the project.</p>
    <p>Please find attached the summary of terms and our proposed timeline for review by your board this month.</p>
    <p>Kind regards from the whole team.</p>
  </div>
  <div class="signature" role="img" aria-label="Handwritten signature of Dara Kolby"></div>
</section>

<section class="sheet card-front" aria-label="Business card front">
  <div class="brand brand-stack"><span class="brand-dot"></span><span>Orvel Crest</span></div>
</section>

<section class="sheet card-back" aria-label="Business card back">
  <div class="band"></div>
  <div class="details">
    <strong>Dara Kolby</strong>COO
    <div class="rule"></div>
    dk@orvelcrest.co.uk<br>27b Hollin Row
  </div>
</section>

<section class="sheet envelope" aria-label="Envelope">
  <svg class="flap" viewBox="0 0 418 52" preserveAspectRatio="none">
    <polygon points="0,0 418,0 418,6 209,52 0,6" fill="var(--olive)"/>
  </svg>
  <div class="brand"><span class="brand-dot"></span>Orvel Crest</div>
</section>

<section class="sheet comp-slip" aria-label="Compliment slip">
  <div class="band"></div>
  <div class="brand brand-stack"><span class="brand-dot"></span><span>Orvel<br>Crest</span></div>
</section>

</body>
</html>
```